Textbook cover for educational dental hygiene seminar

A professional and trendy textbook cover design to be used. 8.5 x 11 with full bleed, cmyk, and a count for binding when designed. Year 2023 displayed, and title BelvaKTO’s Dental Hygiene Academy. Colors- shades of purple, white, and black. Please also use logo. Website www.BelvaKTOPrepCourse.example

For background- maybe ombré, or some sort of trendy design. Display a big tooth on the front.

Colors
6B429C
8869AF
B7A5CE
E3DAEB
F3F0F8

```html
<!DOCTYPE html>
<html lang="en">
<head>
<meta charset="utf-8">
<title>BelvaKTO's Dental Hygiene Academy — 2023 Cover</title>
<link rel="stylesheet" href="https://fonts.googleapis.com/css2?family=Zilla+Slab:wght@700&display=swap">
<style>
  :root {
    --sky-top: #0f0052;
    --sky-mid: #260c9c;
    --sky-low: #3c18cc;
    --band: #190082;
    --strip: #4b1ef8;
    --title: #d3c9ef;
    --seal-core: rgba(40, 14, 150, 0.55);
    --seal-edge: rgba(255, 255, 255, 0.04);
    --seal-name: rgba(255, 255, 255, 0.06);
    --badge: #5a2bff;
  }
  * { margin: 0; padding: 0; box-sizing: border-box; }
  html, body { width: 927px; height: 1200px; overflow: hidden; background: var(--sky-top); }
  .cover {
    position: relative;
    width: 927px;
    height: 1200px;
    background: linear-gradient(to bottom, var(--sky-top) 0%, var(--sky-mid) 50%, var(--sky-low) 78%);
    font-family: "Zilla Slab", Georgia, serif;
    overflow: hidden;
  }
  .backdrop-seal {
    position: absolute;
    left: 50px;
    top: 24px;
    width: 827px;
    height: 876px;
  }
  .title-band {
    position: absolute;
    left: 0;
    top: 940px;
    width: 927px;
    height: 188px;
    background: var(--band);
  }
  .bottom-strip {
    position: absolute;
    left: 0;
    top: 1128px;
    width: 927px;
    height: 72px;
    background: var(--strip);
  }
  .academy-badge {
    position: absolute;
    left: 20px;
    top: 955px;
    width: 152px;
    height: 152px;
  }
  .title {
    position: absolute;
    left: 184px;
    top: 968px;
    color: var(--title);
    font-weight: 700;
    line-height: 1;
  }
  .title-owner { display: block; font-size: 58px; letter-spacing: 3px; }
  .title-name { display: block; font-size: 58px; margin-top: 0; letter-spacing: 3px; }
  .edition-year {
    position: absolute;
    right: 34px;
    top: 983px;
    color: var(--title);
    font-weight: 700;
    font-size: 48px;
    letter-spacing: 3px;
    line-height: 1;
  }
</style>
</head>
<body>
  <main class="cover">
    <svg class="backdrop-seal" viewBox="0 0 827 876" role="img" aria-label="Large faint academy seal with the BelvaKTO's name">
      <defs>
        <radialGradient id="seal-fill" cx="50%" cy="45%" r="55%">
          <stop offset="0%" stop-color="var(--seal-core)"/>
          <stop offset="100%" stop-color="var(--seal-edge)"/>
        </radialGradient>
      </defs>
      <circle cx="413" cy="438" r="408" fill="url(#seal-fill)"/>
      <text x="413" y="476" text-anchor="middle" font-family="Zilla Slab, Georgia, serif" font-weight="700" font-size="118" letter-spacing="4" fill="var(--seal-name)">BelvaKTO's</text>
    </svg>

    <div class="title-band"></div>
    <div class="bottom-strip"></div>

    <svg class="academy-badge" viewBox="0 0 152 152" aria-hidden="true">
      <circle cx="76" cy="76" r="74" fill="var(--badge)"/>
    </svg>

    <h1 class="title">
      <span class="title-owner">BelvaKTO's</span>
      <span class="title-name">Dental Hygiene Academy</span>
    </h1>
    <div class="edition-year">2023</div>
  </main>
</body>
</html>
```